Kelvo Brook Website

Design and implement (fully coded and ready to launch) website for a professional services company - please see the documents attached and send us an email if there are any questions
Target Market(s)
Market to potential clients about the services we offer and be able to reach us for any consulting opportunities
Industry/Entity Type
Professional Service
Coding
Coded - Design and coding required
Number of Pages Required
3 page
Requirements
Must have
- Single page website design that is SEO optimized
Blog Post
Contact US page
Cool images/ logos for the service offering - not fill the website with text/content
Must be professional looking website
Coded website should also look great on different screens - mobile, tablets etc
Nice to have
- Choose easy neutral colors that compliment the logo colors. Having said that don't use every color in the logo for the website design.
Should not have
- Too many colors and several various different fonts

```html
<!DOCTYPE html>
<html lang="en">
<head>
<meta charset="utf-8">
<title>Kelvo Brook — Data Platforms &amp; Analytics</title>
<link href="https://fonts.googleapis.com/css2?family=Poppins:wght@300;400;500;600&display=swap" rel="stylesheet">
<style>
:root{
  --blue:#2a6db5;
  --blue-dark:#1f5a9a;
  --orange:#f26522;
  --ink:#222426;
  --body:#5d6268;
  --muted:#8b9096;
  --band:#f2f6fa;
  --line:#e3e7ec;
  --white:#ffffff;
}
*{margin:0;padding:0;box-sizing:border-box}
html,body{width:1200px;height:3626px;overflow:hidden}
body{font-family:'Poppins',sans-serif;color:var(--ink);background:var(--white);position:relative}
.abs{position:absolute}
.btn{position:absolute;display:flex;align-items:center;justify-content:center;background:var(--blue);color:var(--white);font-size:13px;font-weight:600;letter-spacing:.3px;border-radius:26px;text-decoration:none;height:49px;width:177px}
.btn .arrow{margin-left:6px}

/* header */
.brand{position:absolute;left:108px;display:flex;align-items:center;gap:10px;font-size:24px;font-weight:600;color:var(--ink);letter-spacing:.5px}
.brand .dot{width:14px;height:14px;border-radius:50%;background:var(--orange)}
.nav a{position:absolute;top:49px;font-size:13px;color:#3b3f44;text-decoration:none;letter-spacing:.3px}
.nav a.active{color:var(--orange)}

/* hero */
.hero-title{left:108px;top:224px;font-size:53px;font-weight:600;line-height:60px;color:var(--ink)}
.hero-text{left:108px;top:374px;width:440px;font-size:13.5px;line-height:27px;color:#4a4f55}
.art{position:absolute;border-radius:20px}

/* about */
.about-band{left:0;top:672px;width:1200px;height:591px;background:var(--band)}
.section-title{font-size:30px;font-weight:500;color:var(--ink)}
.center{left:0;width:1200px;text-align:center}
.about-text{left:630px;top:874px;width:462px;font-size:13px;line-height:26.7px;color:var(--body)}

/* services */
.card{position:absolute;top:1418px;width:317px;height:441px;background:var(--white);box-shadow:0 3px 14px rgba(30,60,100,.09);text-align:center}
.card .icon{position:absolute;left:104px;top:52px;width:108px;height:108px;border-radius:50%;background:var(--blue);box-shadow:4px 6px 10px rgba(20,60,110,.25);display:flex;align-items:center;justify-content:center}
.card h3{position:absolute;top:194px;width:100%;font-size:18px;font-weight:400;color:var(--ink)}
.card p{position:absolute;top:236px;left:50px;width:217px;font-size:13.5px;line-height:27px;color:var(--muted)}
.card .btn{left:70px;top:340px}

/* cta */
.cta{left:0;top:1949px;width:1200px;height:167px;background:var(--orange)}
.cta h2{position:absolute;left:108px;top:36px;font-size:30px;font-weight:600;color:var(--white)}
.cta p{position:absolute;left:108px;top:86px;font-size:13px;line-height:20px;color:var(--white)}
.cta .btn{left:915px;top:58px;width:177px;height:51px}

/* blog */
.post{position:absolute;top:2270px;width:317px}
.post .thumb{width:317px;height:212px}
.post h4{margin-top:26px;font-size:17px;font-weight:400;color:var(--ink)}
.post p{margin-top:12px;font-size:11px;line-height:22px;color:var(--muted)}
.post a{display:block;margin-top:12px;font-size:11px;font-weight:600;color:var(--blue);text-decoration:none}

/* contact */
.contact-band{left:0;top:2718px;width:1200px;height:550px;background:linear-gradient(180deg,#f4f7fa,#eef2f6)}
.form-card{left:108px;top:2845px;width:984px;height:359px;background:var(--white);box-shadow:0 4px 18px rgba(30,60,100,.06)}
.field-label{position:absolute;font-size:13px;color:var(--ink)}
.field{position:absolute;border:1px solid var(--line);background:var(--white)}
.submit{position:absolute;left:503px;top:269px;width:434px;height:45px;border-radius:24px;background:var(--blue);color:var(--white);font-size:13px;font-weight:600;display:flex;align-items:center;justify-content:center}

/* footer */
.foot-head{position:absolute;top:3352px;font-size:17px;font-weight:400;color:var(--ink)}
.foot-link{position:absolute;left:431px;font-size:13px;color:#6a6f75}
.copy{left:108px;top:3452px;font-size:11px;color:var(--muted)}
.social{position:absolute;top:3395px;width:14px;height:14px;border-radius:50%;background:#3b3f44}
.info{position:absolute;left:859px;display:flex;gap:8px;font-size:13px;line-height:25px;color:#6a6f75}
.info svg{margin-top:6px;flex:none}
</style>
</head>
<body>

<!-- header -->
<header>
  <a class="brand" style="top:52px" href="#">
    <span class="dot"></span>KELVO BROOK
  </a>
  <nav class="nav">
    <a class="active" href="#" style="left:686px">HOME</a>
    <a href="#" style="left:767px">ABOUT</a>
    <a href="#" style="left:851px">SERVICES</a>
    <a href="#" style="left:951px">BLOG</a>
    <a href="#" style="left:1027px">CONTACT</a>
  </nav>
</header>

<!-- hero -->
<section class="hero">
  <h1 class="abs hero-title">Welcome to<br>Kelvo Brook</h1>
  <p class="abs hero-text">We provides end to end services in architecture, design and development of Data Platforms, Analytic workloads and more.</p>
  <a class="btn" href="#" style="left:108px;top:454px">READ MORE <span class="arrow">→</span></a>
  <div class="art" role="img" aria-label="Isometric illustration of people working around server racks, a laptop, cloud and charts" style="left:563px;top:92px;width:550px;height:528px;background:radial-gradient(circle at 55% 50%,#d9e6f7 0%,#eef4fb 55%,#ffffff 80%)"></div>
</section>

<!-- about -->
<section>
  <div class="abs about-band"></div>
  <div class="art" role="img" aria-label="Isometric illustration of a server tower connected to cloud and network nodes" style="left:82px;top:760px;width:517px;height:416px;background:radial-gradient(circle at 50% 50%,#cfdff3 0%,#e6eef8 55%,#f2f6fa 85%)"></div>
  <h2 class="abs section-title" style="left:630px;top:818px">About Kelvo Brook</h2>
  <p class="abs about-text">Kelvo Brook is a company which intends to be in front of the client's needs, deeply understanding clients' business and delivering and optimizing solutions from the initial phase of scoping the requirements, up to the final delivery, maintenance and continuous upgrade. Kelvo Brook focuses always from the customer perspective to grasp their business need for the IT solutions they deliver.</p>
  <a class="btn" href="#" style="left:630px;top:1059px">READ MORE <span class="arrow">→</span></a>
</section>

<!-- services -->
<section>
  <h2 class="abs section-title center" style="top:1346px">Our Services</h2>

  <article class="card" style="left:108px">
    <div class="icon">
      <svg width="56" height="56" viewBox="0 0 56 56" fill="none" stroke="#fff" stroke-width="2.2">
        <rect x="8" y="12" width="24" height="32" rx="2"/>
        <line x1="13" y1="20" x2="27" y2="20"/><line x1="13" y1="26" x2="27" y2="26"/><line x1="13" y1="32" x2="27" y2="32"/><line x1="13" y1="38" x2="27" y2="38"/>
        <rect x="40" y="8" width="9" height="8"/><rect x="40" y="24" width="9" height="8"/><rect x="40" y="40" width="9" height="8"/>
        <path d="M32 28h4v-16h4M36 28h4M36 28v16h4"/>
      </svg>
    </div>
    <h3>Platform Architecture</h3>
    <p>Kelvo Brook works very closely with clients, product managers and more...</p>
    <a class="btn" href="#">READ MORE <span class="arrow">→</span></a>
  </article>

  <article class="card" style="left:442px">
    <div class="icon">
      <svg width="56" height="56" viewBox="0 0 56 56" fill="none" stroke="#fff" stroke-width="2.2">
        <rect x="8" y="6" width="32" height="42" rx="2"/>
        <rect x="14" y="12" width="20" height="14"/>
        <path d="M18 24v-5M22 24v-8M26 24v-4M30 24v-9"/>
        <line x1="14" y1="32" x2="28" y2="32"/><line x1="14" y1="38" x2="26" y2="38"/>
        <circle cx="38" cy="38" r="7"/><line x1="43" y1="43" x2="50" y2="50"/>
      </svg>
    </div>
    <h3>Data Engineering</h3>
    <p>Kelvo Brook employs the latest proven technologies, best practices and more...</p>
    <a class="btn" href="#">READ MORE <span class="arrow">→</span></a>
  </article>

  <article class="card" style="left:775px">
    <div class="icon">
      <svg width="56" height="56" viewBox="0 0 56 56" fill="none" stroke="#fff" stroke-width="2.2">
        <path d="M16 32a9 9 0 0 1 1-18 12 12 0 0 1 22 3 8 8 0 0 1 1 15z"/>
        <path d="M20 32v8M28 26v16M36 32v8"/>
        <circle cx="20" cy="43" r="3"/><circle cx="28" cy="45" r="3"/><circle cx="36" cy="43" r="3"/>
      </svg>
    </div>
    <h3>Cloud Developments</h3>
    <p>There are numerous technology options, tools, cloud services...</p>
    <a class="btn" href="#">READ MORE <span class="arrow">→</span></a>
  </article>
</section>

<!-- call to action -->
<section class="abs cta">
  <h2>Any Question? Contact Us Now.</h2>
  <p>Lorem ipsum dolor sit amet, consectetur adipiscing elit,<br>sed do eiusmod tempor incididunt...</p>
  <a class="btn" href="#">CONTACT US <span class="arrow">→</span></a>
</section>

<!-- blog -->
<section>
  <h2 class="abs section-title center" style="top:2196px">Latest Blog</h2>

  <article class="post" style="left:108px">
    <div class="thumb" role="img" aria-label="Photo of a person typing on a laptop showing analytics charts" style="background:linear-gradient(135deg,#4a4541 0%,#b9b6b2 55%,#eeeeec 100%)"></div>
    <h4>Lorem ipsum dolor sit amet</h4>
    <p>Lorem ipsum dolor sit amet, consectetur adipis<br>elit, sed do eiusmod tempor incididunt...</p>
    <a href="#">READ MORE →</a>
  </article>

  <article class="post" style="left:442px">
    <div class="thumb" role="img" aria-label="Photo of a laptop screen displaying a data dashboard" style="background:linear-gradient(160deg,#2c3138 0%,#6f7c86 50%,#1d2126 100%)"></div>
    <h4>Lorem ipsum dolor sit amet</h4>
    <p>Lorem ipsum dolor sit amet, consectetur adipis<br>elit, sed do eiusmod tempor incididunt...</p>
    <a href="#">READ MORE →</a>
  </article>

  <article class="post" style="left:775px">
    <div class="thumb" role="img" aria-label="Photo of hands holding a phone over printed charts on a desk" style="background:linear-gradient(135deg,#b88a5e 0%,#e9e4dc 50%,#c49a6c 100%)"></div>
    <h4>Lorem ipsum dolor sit amet</h4>
    <p>Lorem ipsum dolor sit amet, consectetur adipis<br>elit, sed do eiusmod tempor incididunt...</p>
    <a href="#">READ MORE →</a>
  </article>
</section>

<!-- contact -->
<section>
  <div class="abs contact-band"></div>
  <h2 class="abs section-title center" style="top:2770px">Contact Us</h2>
  <form class="abs form-card">
    <label class="field-label" style="left:46px;top:44px">Your Name</label>
    <div class="field" style="left:46px;top:68px;width:433px;height:45px"></div>
    <label class="field-label" style="left:46px;top:143px">Email Address</label>
    <div class="field" style="left:46px;top:169px;width:433px;height:45px"></div>
    <label class="field-label" style="left:46px;top:240px">Subject</label>
    <div class="field" style="left:46px;top:269px;width:433px;height:45px"></div>
    <label class="field-label" style="left:503px;top:41px">Message</label>
    <div class="field" style="left:503px;top:68px;width:434px;height:179px"></div>
    <div class="submit">SUBMIT</div>
  </form>
</section>

<!-- footer -->
<footer>
  <a class="brand" style="top:3370px" href="#">
    <span class="dot"></span>KELVO BROOK
  </a>
  <p class="abs copy">© Kelvo Brook LLC. All Rights Reserved.</p>

  <h5 class="foot-head" style="left:431px">Quick Link</h5>
  <a class="foot-link" style="top:3392px">Home</a>
  <a class="foot-link" style="top:3422px">About</a>
  <a class="foot-link" style="top:3451px">Services</a>
  <a class="foot-link" style="top:3482px">Blog</a>
  <a class="foot-link" style="top:3512px">Contact</a>

  <h5 class="foot-head" style="left:618px">Follow Us</h5>
  <span class="social" style="left:620px" aria-label="Social profile"></span>
  <span class="social" style="left:661px" aria-label="Social profile"></span>
  <span class="social" style="left:703px" aria-label="Social profile"></span>
  <span class="social" style="left:745px" aria-label="Social profile"></span>

  <h5 class="foot-head" style="left:859px">Contact Info</h5>
  <div class="info" style="top:3388px">
    <svg width="12" height="12" viewBox="0 0 24 24" fill="#f26522"><path d="M6.6 10.8a15 15 0 0 0 6.6 6.6l2.2-2.2a1 1 0 0 1 1-.25 11.4 11.4 0 0 0 3.6.6 1 1 0 0 1 1 1V20a1 1 0 0 1-1 1A17 17 0 0 1 3 4a1 1 0 0 1 1-1h3.5a1 1 0 0 1 1 1c0 1.25.2 2.45.6 3.6a1 1 0 0 1-.25 1z"/></svg>
    <span>+1 (555) 014-2290</span>
  </div>
  <div class="info" style="top:3418px">
    <svg width="12" height="12" viewBox="0 0 24 24" fill="#f26522"><path d="M2 5h20v14H2z"/><path d="M2 5l10 8 10-8" stroke="#fff" stroke-width="2" fill="none"/></svg>
    <span>hello@kelvobrook.com</span>
  </div>
  <div class="info" style="top:3448px;width:240px">
    <svg width="12" height="12" viewBox="0 0 24 24" fill="#f26522"><path d="M12 2a7 7 0 0 0-7 7c0 5 7 13 7 13s7-8 7-13a7 7 0 0 0-7-7zm0 9.5A2.5 2.5 0 1 1 12 6.5a2.5 2.5 0 0 1 0 5z"/></svg>
    <span>48 Alder Row, Suite 5, Harlow Bay, Postal 550218</span>
  </div>
</footer>

</body>
</html>
```